Clausewise - Training I Consulting I Review - Related to Contracts/Agreements

We provide legal services, we need a plattform to book video online trainings or local trainings classes and appointments (with calendar feature to select date and see availability at screen), payment over internet, legal document creation over webpage, videos will be produces in the next 3 - 4 moths so this is a place holder item. Participants for the Online trainings shall have a login in area with secured password. Appointments for local trainings and Consulting. Consider Outline in file attached. I can send you also a video with more explanation regarding the purpose.

Target Market(s)

Startup/scale up Software companies that intent to have an international business and need help with their contracts, to sell their products. Sales persons.

Industry/Entity Type

Legal

Coding

Coded - Design and coding required

Number of Pages Required

5+ page

Font styles to use
Serif
Sans Serif

Colors
000000
eeeeee
f5f5f5
ffffff
f8fcfd
3277b5
ecf7fb
cadf82
86cfc6

Requirements
Must have
• See file clausewise attached with outline. Moreover see here first starting point: https://tomas-vendrell.pagebuildr.example/mysite-1 . Main inspiration comes from www.advisoryhub.example from the log in area, see the outline in the file attached with the screen shots. At the end I need someone who can draft the full webpage and maintain it for a yearly fee. It must be simple and well structured layout. Lean. 1st landing page shall not scroll, 2 landing page only a little to see the testimonials and foster of page. There should be a Progress Bar to indicate the booking/selection process. Calendar booking. Easy fast booking.
• I like the colour mix, the feeling and the easy structor of:
• https://www.artmarket.example/design/6374387or
• https://www.artmarket.example/design/6372391 or https://www.artmarket.example/design/6374366
• https://www.vendorgrid.example/en/web-design/belgium-be
• https://www.artmarket.example/design/5896857
• https://www.artmarket.example/design/5902173
• https://www.artmarket.example/design/17197349
• https://www.artmarket.example/design/5464461
• https://www.artmarket.example/design/7180908
Nice to have
• page for evaluation and interview, see outline attached in the file with screen shots. Document upload.
Should not have
• many pictures, long scroll down pages on the 1st and 2nd ladding pages, many colours and forms. No need for news letter, search field, no need for links to Chatterly and other social media (except workNet).

```html
<!DOCTYPE html>
<html lang="en">
<head>
<meta charset="utf-8">
<title>Clausewise – Login</title>
<link rel="stylesheet" href="https://fonts.googleapis.com/css2?family=Arimo:wght@400&family=Barlow:wght@500&display=swap">
<style>
  :root {
    --bg-deep: #0f1a22;
    --bg-mid: #33434f;
    --bg-light: #6d7d86;
    --text-white: #ffffff;
    --field-top: rgba(255,255,255,0.30);
    --field-bottom: rgba(255,255,255,0.08);
    --field-border: rgba(235,235,235,0.75);
    --divider: rgba(80,90,98,0.85);
    --button: #6678bd;
    --button-border: #8f9dd3;
    --checkbox: #2c2f33;
  }
  * { box-sizing: border-box; margin: 0; padding: 0; }
  html, body { width: 1200px; height: 659px; overflow: hidden; background: var(--bg-deep); }
  .login-page {
    position: relative;
    width: 1200px;
    height: 659px;
    overflow: hidden;
    font-family: "Arimo", Arial, sans-serif;
    color: var(--text-white);
  }
  .hero-backdrop {
    position: absolute;
    inset: 0;
    background:
      radial-gradient(ellipse 60% 45% at 50% 30%, rgba(120,140,150,0.55), transparent 70%),
      radial-gradient(ellipse 70% 40% at 45% 75%, rgba(70,90,110,0.45), transparent 75%),
      linear-gradient(180deg, var(--bg-light) 0%, var(--bg-mid) 40%, var(--bg-deep) 100%);
  }
  .brand-title {
    position: absolute;
    left: 0; right: 0;
    top: 166px;
    text-align: center;
    font-family: "Barlow", "Helvetica Neue", sans-serif;
    font-weight: 500;
    font-size: 57px;
    letter-spacing: 0.5px;
    line-height: 1;
  }
  .login-form {
    position: absolute;
    left: 424px;
    top: 267px;
    width: 352px;
  }
  .field {
    position: relative;
    height: 43px;
    border: 1px solid var(--field-border);
    background: linear-gradient(90deg, var(--field-top), var(--field-bottom));
    display: flex;
    align-items: center;
    margin-bottom: 20px;
  }
  .field-label {
    flex: 1;
    padding-left: 12px;
    font-size: 14px;
  }
  .field-icon {
    width: 47px;
    height: 100%;
    border-left: 1px solid var(--field-border);
    display: flex;
    align-items: center;
    justify-content: center;
  }
  .form-actions {
    position: relative;
    height: 28px;
    margin-top: 6px;
    display: flex;
    align-items: center;
    justify-content: space-between;
  }
  .remember {
    display: flex;
    align-items: center;
    font-size: 14px;
  }
  .remember-box {
    width: 21px;
    height: 21px;
    background: var(--checkbox);
    border: 1px solid rgba(255,255,255,0.25);
    margin-right: 13px;
  }
  .login-button {
    width: 65px;
    height: 28px;
    background: var(--button);
    border: 1px solid var(--button-border);
    color: var(--text-white);
    font-family: "Barlow", sans-serif;
    font-weight: 500;
    font-size: 17px;
  }
  .divider {
    height: 3px;
    background: var(--divider);
    margin-top: 20px;
  }
  .form-links {
    display: flex;
    justify-content: space-between;
    align-items: center;
    margin-top: 24px;
    font-size: 14px;
  }
  .back-link { display: flex; align-items: center; gap: 8px; }
</style>
</head>
<body>
<main class="login-page">
  <div class="hero-backdrop" role="img" aria-label="Business people reviewing contract papers in front of a night city skyline"></div>

  <h1 class="brand-title">Clausewise</h1>

  <form class="login-form">
    <div class="field">
      <span class="field-label">First Name</span>
      <span class="field-icon">
        <svg width="20" height="20" viewBox="0 0 20 20" fill="none" stroke="#fff" stroke-width="1.4">
          <circle cx="10" cy="6.5" r="4.5"/>
          <path d="M1.5 19v-1.5c0-3 3-5 8.5-5s8.5 2 8.5 5V19z"/>
        </svg>
      </span>
    </div>
    <div class="field">
      <span class="field-label">Password</span>
      <span class="field-icon">
        <svg width="18" height="22" viewBox="0 0 18 22" fill="none" stroke="#fff" stroke-width="1.6">
          <path d="M4.5 9V6a4.5 4.5 0 0 1 9 0v3"/>
          <rect x="1.5" y="9" width="15" height="11.5" rx="2"/>
          <circle cx="9" cy="14" r="1.4" fill="#fff"/>
          <path d="M9 15v2.5"/>
        </svg>
      </span>
    </div>

    <div class="form-actions">
      <label class="remember"><span class="remember-box"></span>Remember Me</label>
      <button type="button" class="login-button">Login</button>
    </div>

    <div class="divider"></div>

    <div class="form-links">
      <span class="lost-password">Lost your password?</span>
      <span class="back-link">
        <svg width="24" height="12" viewBox="0 0 24 12" fill="none" stroke="#fff" stroke-width="1.6">
          <path d="M23 6H2M7 1L2 6l5 5"/>
        </svg>
        Back to Clausewise
      </span>
    </div>
  </form>
</main>
</body>
</html>
```